Contemporary Elegant Business Card Design for an International Trade Company in the Wine Industry

We need a new business card design for an international trade company in the wine and winemaking industry. The overall feel of the card should be contemporary, upscale, luxurious and elegant. It should communicate confidence and professionalism. The colors should complementary to our logo design (burgundy, gold, and black).
Inspiration: rich velvet tapestry
The card should include the following information:
Business: Brovenna Trading/Shipping, LLC.
Name: Marcus T. Hollenbrand
Title: CEO
Email: mark@brovennatrading.example
Phone: 555-294-6172
www.brovennatrading.example
Updates
Project Deadline Extended
Reason: We'd like the designers that we requested some additional designs from to still submit designs. Thank you!
Industry/Entity Type
Business
Contact Information for Business Card
Title: CEO
Phone: 555-294-6172
www.brovennatrading.example
Look and feel

```html
<!DOCTYPE html>
<html lang="en">
<head>
<meta charset="utf-8">
<title>Brovenna Trading/Shipping, LLC. – Business Card</title>
<link href="https://fonts.googleapis.com/css2?family=Oxygen:wght@400;700&display=swap" rel="stylesheet">
<style>
  :root {
    --burgundy: #8e1a2c;
    --burgundy-deep: #6d1120;
    --burgundy-light: #a5283b;
    --gold: #f1dc9c;
    --gold-deep: #d9a94a;
    --gold-dark: #c18a2a;
    --ink: #1d1a17;
    --white: #ffffff;
    --backdrop: #ece8e2;
  }
  * { box-sizing: border-box; margin: 0; padding: 0; }
  html, body {
    width: 1200px; height: 1023px; overflow: hidden;
    background: var(--backdrop);
    font-family: "Oxygen", Arial, sans-serif;
  }
  .canvas { position: relative; width: 1200px; height: 1023px; }

  .card {
    position: absolute;
    width: 560px; height: 320px;
    overflow: hidden;
    box-shadow: 0 10px 28px rgba(0,0,0,.22);
  }
  .card-front { left: 70px; top: 170px; background: var(--burgundy); }
  .card-back {
    left: 570px; top: 530px;
    background: linear-gradient(135deg, var(--burgundy-light), var(--burgundy) 55%, var(--burgundy-deep));
  }

  .front-art { position: absolute; inset: 0; }

  .brand {
    position: absolute;
    display: flex; align-items: center; gap: 12px;
  }
  .brand-mark { width: 32px; height: 32px; background: var(--burgundy); }
  .brand-name {
    font-weight: 700; color: var(--ink);
    letter-spacing: 1px; line-height: 1;
  }
  .front-brand { right: 30px; top: 18px; }
  .front-brand .brand-name { font-size: 26px; }
  .brand-tagline {
    position: absolute; right: 30px; top: 56px;
    font-size: 9px; font-weight: 700; letter-spacing: 1.4px;
    text-transform: uppercase; color: var(--ink);
  }

  .holder { position: absolute; left: 34px; bottom: 30px; color: var(--white); }
  .holder-name {
    font-size: 19px; font-weight: 700; letter-spacing: 1.2px;
    text-transform: uppercase; line-height: 24px;
  }
  .holder-title { font-size: 12px; margin-top: 2px; opacity: .85; }
  .contact-list { list-style: none; margin-top: 14px; }
  .contact-item {
    display: flex; align-items: center; gap: 8px;
    font-size: 12.5px; line-height: 20px;
  }
  .contact-icon { width: 13px; height: 13px; flex: none; }

  .back-mark {
    position: absolute; left: 56px; top: 52px;
    width: 96px; height: 96px; background: var(--gold-deep);
    box-shadow: 0 4px 10px rgba(0,0,0,.25);
  }
  .back-brand { position: absolute; right: 44px; bottom: 70px; text-align: right; color: var(--white); }
  .back-brand .brand-name { color: var(--white); font-size: 52px; letter-spacing: 3px; }
  .back-tagline {
    margin-top: 8px; font-size: 14px; font-weight: 700;
    letter-spacing: 2px; text-transform: uppercase;
  }
</style>
</head>
<body>
<main class="canvas">

  <section class="card card-front" aria-label="Business card front">
    <svg class="front-art" viewBox="0 0 560 320" width="560" height="320" aria-hidden="true">
      <defs>
        <linearGradient id="goldPanel" x1="0" y1="0" x2="1" y2="1">
          <stop offset="0" stop-color="#f6e6b0"/>
          <stop offset="1" stop-color="#eccf84"/>
        </linearGradient>
      </defs>
      <polygon points="0,0 560,0 560,78 0,158" fill="url(#goldPanel)"/>
    </svg>
    <svg class="front-art" viewBox="0 0 560 320" width="560" height="320" role="img" aria-label="Faint world map texture across the card">
      <defs>
        <radialGradient id="mapTint" cx=".45" cy=".45" r=".6">
          <stop offset="0" stop-color="#c18a2a" stop-opacity=".18"/>
          <stop offset="1" stop-color="#c18a2a" stop-opacity="0"/>
        </radialGradient>
      </defs>
      <rect width="560" height="320" fill="url(#mapTint)"/>
    </svg>

    <div class="brand front-brand">
      <span class="brand-mark"></span>
      <span class="brand-name">BROVENNA</span>
    </div>
    <p class="brand-tagline">Trading and Shipping</p>

    <div class="holder">
      <h1 class="holder-name">Marcus T. Hollenbrand</h1>
      <p class="holder-title">CEO</p>
      <ul class="contact-list">
        <li class="contact-item">
          <svg class="contact-icon" viewBox="0 0 14 14" aria-hidden="true"><rect width="14" height="14" rx="2" fill="#fff"/><path d="M4 3.5c.6-.4 1.2-.3 1.5.3l.6 1.2c.2.4 0 .8-.3 1l-.4.3c.4.9 1 1.5 1.9 1.9l.3-.4c.3-.3.7-.5 1-.3l1.2.6c.6.3.7.9.3 1.5-.6.8-1.5.9-2.5.4C5.8 9.3 4.7 8.2 4 6.4 3.5 5.2 3.4 4.2 4 3.5z" fill="#8e1a2c"/></svg>
          555-294-6172
        </li>
        <li class="contact-item">
          <svg class="contact-icon" viewBox="0 0 14 14" aria-hidden="true"><rect width="14" height="14" rx="2" fill="#fff"/><rect x="3" y="4" width="8" height="6" fill="none" stroke="#8e1a2c" stroke-width="1.1"/><path d="M3 4l4 3.2L11 4" fill="none" stroke="#8e1a2c" stroke-width="1.1"/></svg>
          mark@brovennatrading.example
        </li>
        <li class="contact-item">
          <svg class="contact-icon" viewBox="0 0 14 14" aria-hidden="true"><rect width="14" height="14" rx="2" fill="#fff"/><circle cx="7" cy="7" r="3.8" fill="none" stroke="#8e1a2c" stroke-width="1"/><path d="M3.2 7h7.6M7 3.2c-1.6 2.2-1.6 5.4 0 7.6M7 3.2c1.6 2.2 1.6 5.4 0 7.6" fill="none" stroke="#8e1a2c" stroke-width=".9"/></svg>
          www.brovennatrading.example
        </li>
      </ul>
    </div>
  </section>

  <section class="card card-back" aria-label="Business card back">
    <span class="back-mark"></span>
    <div class="back-brand">
      <p class="brand-name">BROVENNA</p>
      <p class="back-tagline">Trading and Shipping</p>
    </div>
  </section>

</main>
</body>
</html>
```